A start up special flyer design!

Hi All - Have updated the attachment content - This is the info required for the designs.
I need a catchy flyer to send out to a few areas to advertise the start of my plumbing business!
The flyer will contain an offer for customers, which will need to have some key details on it. See attached. Feel free to fit these criteria into the flyer given your knowledge on design and messaging principles. Key thing to get across to customers is the discount and special offer, and that it is a start up offer.
I have a logo that needs to be on the flyer as well - let me know what format you require and I will send through to you.
The color scheme needs to be blue / grey / black / white.
Let me know if you have any questions.
I

```html
<!DOCTYPE html>
<html lang="en">
<head>
<meta charset="utf-8">
<title>Danny Flow Plumbing – Start-up Offer Flyer</title>
<link rel="stylesheet" href="https://fonts.googleapis.com/css2?family=Montserrat:wght@600;800&family=Open+Sans:wght@400&family=Roboto+Condensed:wght@300;400;700&display=swap">
<style>
  :root {
    --blue: #1d5fb8;
    --blue-deep: #0f3f8f;
    --blue-bright: #2f7fe0;
    --ink: #1e1e1e;
    --grey: #a2a5a9;
    --grey-light: #dcdee0;
    --white: #ffffff;
  }
  * { margin: 0; padding: 0; box-sizing: border-box; }
  html, body { width: 869px; height: 1200px; overflow: hidden; background: var(--white); }
  .flyer { position: relative; width: 869px; height: 1200px; overflow: hidden; background: var(--white); font-family: "Open Sans", sans-serif; color: var(--ink); }
  .abs { position: absolute; }

  .hero-photo { left: 250px; top: 0; width: 619px; height: 560px;
    background: linear-gradient(90deg, rgba(255,255,255,1) 0%, rgba(214,220,228,0.8) 25%, #9aa6b5 55%, #5d6f86 100%); }
  .shapes { left: 0; top: 0; width: 869px; height: 1200px; }

  .brand { left: 32px; top: 40px; width: 316px; text-align: center; color: var(--blue); font-family: "Montserrat", sans-serif; font-weight: 600; }
  .brand-dot { display: block; width: 26px; height: 26px; margin: 0 auto 14px; border-radius: 50%; background: var(--blue); }
  .brand-name { font-size: 29px; letter-spacing: 1px; line-height: 1; }
  .brand-sub { font-size: 15px; letter-spacing: 7px; margin-top: 6px; }

  .headline { left: 40px; top: 548px; font-family: "Roboto Condensed", sans-serif; }
  .headline-lead { font-size: 72px; font-weight: 700; color: var(--blue); line-height: 0.95; letter-spacing: -0.5px; }
  .headline-main { font-size: 60px; font-weight: 300; color: var(--ink); line-height: 1.1; }
  .headline-tail { font-family: "Montserrat", sans-serif; font-size: 25px; font-weight: 800; color: var(--blue-deep); margin-top: 4px; letter-spacing: 0.5px; }

  .pill { left: 0; height: 35px; background: var(--blue); color: var(--white); border-radius: 0 18px 18px 0;
    font-family: "Montserrat", sans-serif; font-weight: 600; font-size: 18px; letter-spacing: 1px; line-height: 35px; padding-left: 42px; }
  .pill-offers { top: 742px; width: 178px; }
  .pill-validity { top: 905px; width: 182px; }

  .offer-list { left: 44px; top: 790px; width: 320px; list-style: none; font-size: 17px; line-height: 23px; }
  .offer-list li { position: relative; padding-left: 20px; margin-bottom: 4px; }
  .offer-list li::before { content: ""; position: absolute; left: 0; top: 7px; width: 11px; height: 11px; border-radius: 50%; background: var(--blue); }

  .validity-dates { left: 32px; top: 952px; font-family: "Roboto Condensed", sans-serif; font-weight: 700; font-size: 24px; color: var(--ink); }
  .validity-dates em { font-style: normal; color: var(--blue-deep); }
  .validity-note { left: 32px; top: 985px; font-size: 17px; }

  .quote-bar { left: 0; top: 1020px; width: 372px; height: 68px; background: var(--blue); color: var(--white);
    font-family: "Roboto Condensed", sans-serif; font-weight: 700; font-size: 19px; line-height: 27px; padding: 7px 0 0 32px; }

  .booking { left: 32px; top: 1098px; width: 320px; font-size: 17px; line-height: 27px; text-align: justify; }

  .badge-text { left: 525px; top: 530px; width: 300px; text-align: center; color: var(--white); }
  .badge-big { font-family: "Roboto Condensed", sans-serif; font-weight: 700; font-size: 50px; line-height: 1; }
  .badge-mid { font-family: "Montserrat", sans-serif; font-weight: 800; font-size: 24px; margin-top: 6px; }
  .badge-low { font-family: "Roboto Condensed", sans-serif; font-weight: 400; font-size: 40px; line-height: 1.1; }

  .service-list { left: 516px; top: 818px; width: 330px; list-style: none; color: var(--white); font-size: 17px; line-height: 23px; }
  .service-list li { position: relative; padding-left: 22px; margin-bottom: 3px; }
  .service-list li.plain { padding-left: 0; margin-left: -8px; }
  .service-list li:not(.plain)::before { content: ""; position: absolute; left: 0; top: 6px; width: 12px; height: 12px; border-radius: 50%; background: var(--white); }
  .service-list li:nth-child(2) { margin-left: -30px; }

  .call-label { left: 398px; top: 986px; font-family: "Roboto Condensed", sans-serif; font-weight: 700; font-size: 46px; color: var(--blue-deep); }
  .call-number { left: 398px; top: 1044px; font-family: "Roboto Condensed", sans-serif; font-weight: 700; font-size: 44px; color: var(--white); letter-spacing: 0.5px; }
  .contact { left: 378px; top: 1124px; color: var(--white); font-size: 17px; line-height: 28px; }
  .contact-row { display: flex; align-items: center; gap: 6px; }

  .worker-photo { left: 680px; top: 950px; width: 186px; height: 248px; border-radius: 90px 90px 8px 8px;
    background: linear-gradient(180deg, #8fa3bd 0%, #5c7aa3 55%, #6b5a48 100%); }
</style>
</head>
<body>
<main class="flyer">

  <div class="abs hero-photo" role="img" aria-label="Photo of a plumber kneeling beside a bathtub, working on pipes with a toolbox"></div>

  <svg class="abs shapes" viewBox="0 0 869 1200" aria-hidden="true">
    <defs>
      <linearGradient id="greyBand" x1="0" y1="0" x2="1" y2="0">
        <stop offset="0" stop-color="#c9ccd0"/><stop offset="1" stop-color="#eceef0"/>
      </linearGradient>
      <linearGradient id="silver" x1="0" y1="0" x2="1" y2="1">
        <stop offset="0" stop-color="#f4f5f7"/><stop offset="0.5" stop-color="#b9bdc3"/><stop offset="1" stop-color="#eef0f2"/>
      </linearGradient>
      <radialGradient id="badgeFill" cx="0.4" cy="0.35" r="0.75">
        <stop offset="0" stop-color="#2f7fe0"/><stop offset="1" stop-color="#0f3f8f"/>
      </radialGradient>
    </defs>
    <path d="M0,420 C170,360 390,400 560,540 L869,470 L869,1200 L0,1200 Z" fill="var(--blue)"/>
    <path d="M0,452 C180,402 390,442 545,572 L869,505 L869,1200 L0,1200 Z" fill="url(#greyBand)"/>
    <path d="M540,580 L869,515 L869,1200 L356,1200 L356,1020 C370,880 430,720 540,610 Z" fill="var(--grey)"/>
    <path d="M548,600 C440,720 388,880 372,1020 L392,1020 C412,880 470,742 568,632 Z" fill="var(--blue)"/>
    <path d="M0,488 C200,448 400,505 525,625 C430,725 378,900 368,1020 L368,1200 L0,1200 Z" fill="var(--white)"/>
    <circle cx="675" cy="641" r="152" fill="url(#silver)"/>
    <circle cx="675" cy="641" r="138" fill="var(--white)"/>
    <circle cx="675" cy="641" r="130" fill="url(#badgeFill)"/>
  </svg>

  <header class="abs brand">
    <span class="brand-dot"></span>
    <div class="brand-name">DANNY FLOW</div>
    <div class="brand-sub">PLUMBING</div>
  </header>

  <div class="abs badge-text">
    <div class="badge-big">15% OFF</div>
    <div class="badge-mid">YOUR</div>
    <div class="badge-low">OVERALL BILL</div>
  </div>

  <h1 class="abs headline">
    <div class="headline-lead">DELIVERING</div>
    <div class="headline-main">QUALITY WORK</div>
    <div class="headline-tail">AT A DECENT PRICE</div>
  </h1>

  <div class="abs pill pill-offers">OFFERS</div>
  <ul class="abs offer-list">
    <li>No GST payable, saving you additional 10% on your bill</li>
    <li>Plus, a free hot water health check and replacement quote</li>
  </ul>

  <div class="abs pill pill-validity">VALIDITY</div>
  <p class="abs validity-dates"><em>15 August</em> 2016 to <em>15 October</em> 2016</p>
  <p class="abs validity-note">Valid until 30 September 2016</p>

  <div class="abs quote-bar">QUOTE VALID FOR 12 MONTHS<br>FROM THE QUOTE DATE</div>

  <p class="abs booking">To make an appointment, call or email Danny, or alternatively make a booking directly on the website</p>

  <ul class="abs service-list">
    <li>All plumbing, draining, and gasfitting works</li>
    <li>Quality work at a decent price</li>
    <li class="plain">Local plumber</li>
  </ul>

  <p class="abs call-label">CALL TODAY</p>
  <p class="abs call-number">0400 118 264</p>

  <div class="abs contact">
    <div class="contact-row">
      <svg width="14" height="11" viewBox="0 0 14 11" aria-hidden="true"><rect x="0.5" y="0.5" width="13" height="10" fill="none" stroke="#fff"/><path d="M0.5,0.5 L7,6 L13.5,0.5" fill="none" stroke="#fff"/></svg>
      danny@dannyflowplumbing.com
    </div>
    <div class="contact-row">
      <svg width="14" height="14" viewBox="0 0 14 14" aria-hidden="true"><circle cx="7" cy="7" r="6.3" fill="none" stroke="#fff"/><path d="M0.7,7 H13.3 M7,0.7 C3,4 3,10 7,13.3 M7,0.7 C11,4 11,10 7,13.3" fill="none" stroke="#fff"/></svg>
      www.dannyflowplumbing.com
    </div>
  </div>

  <div class="abs worker-photo" role="img" aria-label="Photo of a smiling plumber crouching with a tool belt and a spirit level"></div>

</main>
</body>
</html>
```